Dietary supplement package design

We need a design for a range of dietary supplements mentioned below. The colors can be derived from the attached company logo and the package is a plastic bottle for medicines use (attached is a sample). All products will have the same package design and color with a permissible slight change to product name and associated picture/artwork (if any). Please avoid using pictures of humans or animals. We expect to see a label with three panels:
1. Left panel containing instructions, warnings and other information.
2. Front panel containing products name and its unique look
3. Right panel containing nutrient/ingredient information table and address.
The label will dual language (Arabic/English) and we have no issue to use special colors, i.e. UV, gold or silver.
Products names are:
1. Ginkgo biloba
2. Slimming formula
3. Fat Absorber
4. Glutathione
5. Royal Jelly
6. Vitamin D
Consumers and health care professionals
Healthcare

```html
<!DOCTYPE html>
<html lang="en">
<head>
<meta charset="utf-8">
<title>Slimming Formula Label</title>
<link rel="stylesheet" href="https://fonts.googleapis.com/css2?family=PT+Sans:wght@400;700&family=Allura&display=swap">
<style>
  :root {
    --page: #ffffff;
    --label: #f1f1f2;
    --navy: #0b0a4d;
    --brand-blue: #2f57a6;
    --text-blue: #2d3f96;
    --edge: #b9b6d6;
    --white: #ffffff;
  }
  * { margin: 0; padding: 0; box-sizing: border-box; }
  html, body { width: 1200px; height: 913px; overflow: hidden; background: var(--page); }
  body { position: relative; font-family: "PT Sans", Arial, sans-serif; color: var(--text-blue); }

  .label {
    position: absolute; left: 151px; top: 318px; width: 930px; height: 289px;
    background: var(--label); border-left: 1px solid var(--edge); border-right: 1px solid var(--edge);
  }
  .label__band { position: absolute; left: 0; width: 100%; height: 9px; background: var(--navy); }
  .label__band--top { top: 0; }
  .label__band--bottom { bottom: 0; }

  .panel-info { position: absolute; left: 8px; top: 26px; width: 268px; font-size: 12.5px; line-height: 1.3; }
  .panel-info .product-ref { font-weight: 700; }
  .section-title { font-size: 16px; margin: 18px 0 6px 3px; }
  .producer { display: flex; align-items: flex-end; gap: 8px; margin: 8px 0 0 8px; }
  .producer__label { font-size: 9px; font-weight: 700; margin-bottom: 12px; }
  .producer__mark { display: flex; flex-direction: column; align-items: center; gap: 2px; }
  .producer__square { width: 14px; height: 14px; background: var(--navy); }
  .producer__name { font-size: 14px; font-weight: 700; color: var(--brand-blue); line-height: 1; }

  .panel-front {
    position: absolute; left: 273px; top: 9px; width: 366px; height: 239px; background: var(--brand-blue);
  }
  .panel-front__emblem {
    position: absolute; left: 119px; top: 13px; width: 72px; height: 72px; background: var(--white); border-radius: 6px;
  }
  .panel-front__name {
    position: absolute; color: var(--white); font-family: "Allura", cursive; font-size: 58px; line-height: 1; transform: rotate(-4deg);
  }
  .panel-front__name--first { left: 54px; top: 102px; }
  .panel-front__name--second { left: 150px; top: 150px; }

  .panel-instructions { position: absolute; left: 654px; top: 28px; width: 264px; font-size: 12.5px; line-height: 1.3; }
  .panel-instructions .section-title { margin: 0 0 14px 0; }
</style>
</head>
<body>
  <div class="label">
    <div class="label__band label__band--top"></div>

    <section class="panel-info">
      <p><span class="product-ref">Slimming Formula</span> is Lorem ipsum dolor sit amet, consectetur adipiscing elit. Praesent accumsan, risus non dapibus consequat, mauris est bibendum tellus, in aliquam elit nisl at diam.</p>
      <h2 class="section-title">Ingredients :</h2>
      <p>coconut oil, beeswax, soy lecithin, and eight all natural botanical oils - cannabis, lavender, eucalyptus, ginkgo biloba, rosemary, cinnamon, clove, and lemon</p>
      <div class="producer">
        <span class="producer__label">Produced by</span>
        <span class="producer__mark">
          <span class="producer__square"></span>
          <span class="producer__name">Meridian</span>
        </span>
      </div>
    </section>

    <section class="panel-front">
      <div class="panel-front__emblem" role="img" aria-label="Product emblem artwork"></div>
      <span class="panel-front__name panel-front__name--first">Slimming</span>
      <span class="panel-front__name panel-front__name--second">Formula</span>
    </section>

    <section class="panel-instructions">
      <h2 class="section-title">Instruction :</h2>
      <p>Lorem ipsum dolor sit amet, consectetur adipiscing elit. Praesent accumsan, risus non dapibus consequat, mauris est bibendum tellus, in aliquam elit nisl at diam. Curabitur ac viverra dui. Maecenas quis nulla interdum, varius massa sit amet, congue est. Cras purus nulla, pharetra vel consequat at, mattis sit amet justo. Sed lacinia ex eget augue porttitor iaculis. Vestibulum et lectus ac dolor ullamcorper feugiat.</p>
    </section>

    <div class="label__band label__band--bottom"></div>
  </div>
</body>
</html>
```